Packaging design for Lumo Drift Style snack

Looking for food product packaging. Our product is a sweet, salty, and savory lumo drift style snack. We would like to see designs that use the colors yellow and red and any color that compliments them is welcomed. Preferably pastel if possible to be more modern contemporary but with an appeal to kids to young adults. The final design should communicate spark curiosity, hunger, and addiction.

Target Market(s)

12 - 60 year olds. Mainly targeting younger kids but also to older adults

Industry/Entity Type

Food & Beverage

Colors
FFF300
FFF600
FEFA6F
FFFEC7
FFFEE8
FFC000
F8CF3A
FAE287
FDF2CF
FEFAEE
F0912C
F2A743
F7CA91
FBE8D2
FDF5EE
EE7325
F08F49
F5BC92
FAE3D3
FDF4ED

```html
<!DOCTYPE html>
<html lang="en">
<head>
<meta charset="UTF-8">
<title>Vela Crunch – Cereal Mix Pack</title>
<link rel="stylesheet" href="https://fonts.googleapis.com/css2?family=Montserrat:wght@700;800&family=Bangers&family=Kaushan+Script&display=swap">
<style>
  :root {
    --page: #ffffff;
    --pack-yellow: #ffd500;
    --snack-cream: #efe0b8;
    --snack-light: #e6cf94;
    --snack-gold: #dcb45e;
    --snack-toast: #c98c3c;
    --snack-rust: #b8652a;
    --snack-shadow: #8a6a3a;
    --brand-red: #e3131b;
    --cereal-red: #e8261c;
    --cereal-pink: #f04fd8;
    --mix-brown: #4a0a0a;
  }
  * { margin: 0; padding: 0; box-sizing: border-box; }
  html, body {
    width: 679px;
    height: 1200px;
    overflow: hidden;
    background: var(--page);
  }
  .pack {
    position: absolute;
    left: 32px;
    top: 34px;
    width: 615px;
    height: 1126px;
    background: var(--pack-yellow);
    overflow: hidden;
  }
  .snack-photo {
    position: absolute;
    left: 0;
    top: 0;
    width: 100%;
    height: 720px;
    background:
      linear-gradient(to bottom,
        rgba(255,213,0,0) 0%,
        rgba(255,213,0,0.05) 25%,
        rgba(255,213,0,0.35) 50%,
        rgba(255,213,0,0.7) 72%,
        var(--pack-yellow) 100%),
      radial-gradient(ellipse 90px 60px at 8% 6%, rgba(184,101,42,0.75), transparent 70%),
      radial-gradient(ellipse 80px 70px at 95% 5%, rgba(138,106,58,0.8), transparent 70%),
      radial-gradient(ellipse 110px 80px at 35% 10%, rgba(239,224,184,0.9), transparent 70%),
      radial-gradient(ellipse 90px 70px at 62% 12%, rgba(201,140,60,0.7), transparent 70%),
      radial-gradient(ellipse 120px 90px at 80% 25%, rgba(230,207,148,0.9), transparent 70%),
      radial-gradient(ellipse 100px 80px at 18% 30%, rgba(220,180,94,0.9), transparent 70%),
      radial-gradient(ellipse 90px 70px at 55% 32%, rgba(239,224,184,0.85), transparent 70%),
      radial-gradient(ellipse 70px 55px at 72% 45%, rgba(184,101,42,0.6), transparent 70%),
      radial-gradient(ellipse 110px 80px at 30% 50%, rgba(201,140,60,0.6), transparent 70%),
      radial-gradient(ellipse 120px 80px at 90% 55%, rgba(220,180,94,0.7), transparent 70%),
      linear-gradient(160deg, var(--snack-light) 0%, var(--snack-gold) 40%, var(--snack-toast) 70%, var(--snack-gold) 100%);
  }
  .brand {
    position: absolute;
    left: 176px;
    top: 480px;
    width: 330px;
    font-family: "Montserrat", sans-serif;
    font-weight: 800;
    line-height: 1;
    color: var(--brand-red);
  }
  .brand .brand-main {
    display: block;
    font-size: 112px;
    letter-spacing: -3px;
  }
  .brand .brand-sub {
    display: block;
    text-align: right;
    font-size: 46px;
    margin-top: -4px;
  }
  .product-name {
    position: absolute;
    left: 0;
    width: 100%;
    top: 718px;
    text-align: center;
    font-weight: normal;
  }
  .product-name .cereal {
    display: inline-block;
    font-family: "Bangers", sans-serif;
    font-size: 100px;
    line-height: 1;
    letter-spacing: 3px;
    transform: scaleX(1.7);
    background: linear-gradient(to bottom, var(--cereal-red) 0%, var(--cereal-red) 38%, var(--cereal-pink) 72%);
    -webkit-background-clip: text;
    background-clip: text;
    color: transparent;
  }
  .product-name .mix {
    display: block;
    margin-top: -4px;
    font-family: "Kaushan Script", cursive;
    font-size: 124px;
    line-height: 1;
    color: var(--mix-brown);
  }
  .base-band {
    position: absolute;
    left: 0;
    bottom: 0;
    width: 100%;
    height: 68px;
    background: var(--brand-red);
  }
  .net-weight {
    position: absolute;
    left: 228px;
    top: 0;
    width: 156px;
    height: 48px;
    background: var(--pack-yellow);
    border-radius: 0 0 14px 14px;
    font-family: "Montserrat", sans-serif;
    font-weight: 800;
    font-size: 34px;
    line-height: 48px;
    text-align: center;
    color: var(--brand-red);
  }
</style>
</head>
<body>
  <main class="pack">
    <div class="snack-photo" role="img" aria-label="Close-up photo of a heap of toasted cereal squares, pretzels and savoury crunchy bits with herbs"></div>
    <div class="brand">
      <span class="brand-main">Vela</span>
      <span class="brand-sub">Crunch</span>
    </div>
    <h1 class="product-name">
      <span class="cereal">CEREAL</span>
      <span class="mix">Mix</span>
    </h1>
    <div class="base-band">
      <div class="net-weight">250g</div>
    </div>
  </main>
</body>
</html>
```